New Snazzy yet professinoal business card updated for todays consumer for a Real Estate Professional

I work in a family owned real estate business where we specialize in sales (buyer/seller) and property management. I would like a snazzy business card that will set me apart from other agents while maintaining its professional appearance. I would like to use the front and back of the card incorporating the business logo on the front with pictures and my personal logo on the back side. I have to have the TPXN symbol which I have attached. Card must be easy to read, distinguishable, and professional. Old card with contact information attached. My email has changed to Milo@MiloBrentwickHomes.com

Target Market(s)

Home Sellers, Home Buyers, Business Professionals, Marketing Services,

Industry/Entity Type

Real Estate Agent

Contact Information for Business Card

Professional business card to stand apart from other agents while maintaining a professional appeal.

Font styles to use
Serif

Colors
ec1f27
fbee3e
0455a3

Requirements
Must have
• Must have contact information clear, easy to read. legible
Nice to have
• My picture.

```html
<!DOCTYPE html>
<html lang="en">
<head>
<meta charset="utf-8">
<title>Milo Brentwick – Business Card</title>
<link href="https://fonts.googleapis.com/css2?family=Ubuntu:wght@400;500&family=PT+Sans:wght@400;700&display=swap" rel="stylesheet">
<style>
  :root {
    --page: #ecebe8;
    --blue: #2f63b0;
    --navy: #2d4386;
    --ink: #2f3f8c;
    --red: #b8303f;
    --yellow: #f8ee3c;
    --card-light: #ffffff;
    --card-shade: #d9d9d9;
    --badge: #cfe0f3;
  }
  * { margin: 0; padding: 0; box-sizing: border-box; }
  html, body { width: 1200px; height: 1000px; overflow: hidden; background: var(--page); }
  .canvas { position: relative; width: 1200px; height: 1000px; }
  .card {
    position: absolute; width: 745px; height: 424px; overflow: hidden;
    background: radial-gradient(ellipse at 50% 45%, var(--card-light) 30%, var(--card-shade) 100%);
    box-shadow: 0 3px 8px rgba(0,0,0,.25);
  }
  .card--front { left: 240px; top: 18px; }
  .card--back { left: 238px; top: 553px; }
  .card__band { position: absolute; left: 0; top: 0; width: 745px; height: 160px; }
  .firm-name {
    position: absolute; left: 64px; top: 152px; width: 440px;
    font-family: "Ubuntu", sans-serif; font-weight: 400; font-size: 46px; line-height: 1.05;
    color: var(--red); letter-spacing: 1px; white-space: nowrap;
  }
  .portrait {
    position: absolute; left: 536px; top: 108px; width: 142px; height: 172px;
    border: 5px solid var(--yellow);
    background: linear-gradient(160deg, #8a98a6 0%, #5e6b78 55%, #2a2f38 100%);
  }
  .agent { position: absolute; left: 490px; top: 282px; width: 236px; text-align: center; font-family: "PT Sans", sans-serif; }
  .agent__name { font-size: 20px; color: var(--red); letter-spacing: .5px; line-height: 1; }
  .agent__title { font-size: 11.5px; color: var(--ink); letter-spacing: .5px; margin-top: 2px; }
  .contact { position: absolute; font-family: "PT Sans", sans-serif; font-size: 19px; color: var(--ink); white-space: nowrap; }
  .contact::before {
    content: ""; position: absolute; left: -15px; top: 3px; width: 9px; height: 9px; background: var(--yellow);
  }
  .address-bar {
    position: absolute; left: 0; top: 382px; width: 745px; height: 28px; background: var(--yellow);
    font-family: "PT Sans", sans-serif; font-weight: 700; font-size: 15px; color: var(--navy);
    padding: 4px 0 0 59px; white-space: nowrap;
  }
  .listing-badge { position: absolute; left: 557px; top: 389px; width: 43px; height: 19px; background: var(--badge); border: 1px solid #9bb6d8; }
  .personal-mark { position: absolute; left: 190px; top: 175px; display: flex; align-items: center; gap: 18px; }
  .personal-mark__dot { width: 26px; height: 26px; border-radius: 50%; background: var(--red); }
  .personal-mark__name { font-family: "Ubuntu", sans-serif; font-weight: 400; color: var(--navy); }
  .personal-mark__main { font-size: 38px; line-height: 1; }
  .personal-mark__sub { font-size: 16px; letter-spacing: 7px; margin-top: 6px; text-align: right; }
</style>
</head>
<body>
<div class="canvas">

  <section class="card card--front">
    <svg class="card__band" viewBox="0 0 745 160" aria-hidden="true">
      <path d="M0,0 H745 V78 Q420,-22 0,112 Z" fill="var(--blue)"/>
      <path d="M0,112 Q420,-22 745,78 V102 Q420,8 0,146 Z" fill="var(--navy)"/>
    </svg>
    <div class="firm-name">Oakline Realty LLC</div>
    <div class="portrait" role="img" aria-label="Portrait photo of the agent"></div>
    <div class="agent">
      <div class="agent__name">MILO BRENTWICK</div>
      <div class="agent__title">REALTOR, MBA, MPH</div>
    </div>
    <div class="contact" style="left:58px; top:320px;">Office: 555 210 4410</div>
    <div class="contact" style="left:285px; top:320px;">Cell: 555 318 2276</div>
    <div class="contact" style="left:58px; top:357px;">Fax: 555 210 4417</div>
    <div class="contact" style="left:285px; top:357px;">Email: Milo@MiloBrentwickHomes.com</div>
    <div class="address-bar">Address: 48 Larkmoor Plaza&nbsp; Fenwick, Mississippi 39400</div>
    <div class="listing-badge" role="img" aria-label="TPXN listing badge"></div>
  </section>

  <section class="card card--back">
    <svg class="card__band" viewBox="0 0 745 160" aria-hidden="true">
      <path d="M0,0 H745 V78 Q420,-22 0,112 Z" fill="var(--blue)"/>
      <path d="M0,112 Q420,-22 745,78 V102 Q420,8 0,146 Z" fill="var(--navy)"/>
    </svg>
    <div class="personal-mark">
      <div class="personal-mark__dot"></div>
      <div class="personal-mark__name">
        <div class="personal-mark__main">MILO BRENTWICK</div>
        <div class="personal-mark__sub">HOMES</div>
      </div>
    </div>
  </section>

</div>
</body>
</html>
```